Eye-catching Yellow Page Ad for Attorney's Office

We need a phone book advertisement for our law office. We practice workers' compensation law, and our clientele consists exclusively of individuals who have been injured on the job. The dimensions of the print ad will be 6" W X 4.54" H.

We've had our current ad for several years, and wanted to get a new one that has been designed by a professional. Being that it's an ad for a law firm, it needs to be professional looking, but we're hoping to have something that looks a little more modern and has eye-catching appeal. We like the text that is included in the ad, and we want to make sure our phone number is very visible. No real preference for color scheme.

I've attached a copy of our current ad. All the information included in there is accurate. Our office name is Thornbury & Lisle, PLLC. The ethical rules for attorney advertising require the PLLC to be included in the ad, but it can be smaller than the other text (see our current ad).

Target Market(s)

Our potential clients are injured workers looking for legal representation in their workers' compensation claim.

Industry/Entity Type

Attorney

Font styles to use
Serif
Sans Serif

Requirements
Must have
• Professional, but stands out from the crowd
Nice to have
• Clean modern design
Should not have
• We don't want it to be too crowded or over-worked.

```html
<!DOCTYPE html>
<html lang="en">
<head>
<meta charset="utf-8">
<title>Thornbury &amp; Lisle, PLLC – Workers' Compensation</title>
<link rel="stylesheet" href="https://fonts.googleapis.com/css2?family=Didact+Gothic&family=Tinos:ital,wght@0,700;1,700&family=Open+Sans:ital,wght@0,400;0,700;1,700&family=Arimo:wght@400;700&display=swap">
<style>
  :root {
    --ink: #000000;
    --ad-yellow: #f7f300;
    --title-yellow: #f4f000;
    --alert-red: #ee1111;
    --photo-dark: #5a4230;
    --photo-light: #b58a5a;
  }
  html, body { margin: 0; padding: 0; overflow: hidden; }
  .ad {
    position: relative;
    width: 1200px; height: 900px;
    background: var(--ad-yellow);
    overflow: hidden;
    color: var(--ink);
  }
  .masthead {
    position: absolute; left: 0; top: 0; width: 1200px; height: 120px;
    background: var(--ink);
    overflow: hidden;
  }
  .firm-name {
    position: absolute; left: 0; width: 1200px; top: -20px;
    text-align: center;
    font-family: "Didact Gothic", sans-serif;
    font-size: 84px; line-height: 96px;
    color: var(--title-yellow);
    margin: 0; font-weight: 400;
  }
  .firm-name sup { font-size: 28px; vertical-align: 46px; margin-left: -2px; }
  .practice {
    position: absolute; left: 0; width: 1266px; top: 136px;
    text-align: center; margin: 0;
    font-family: "Tinos", serif; font-weight: 700;
    font-size: 58px; line-height: 66px; letter-spacing: 1px;
  }
  .credential {
    position: absolute; left: 0; width: 1220px; top: 197px;
    text-align: center; margin: 0;
    font-family: "Tinos", serif; font-style: italic; font-weight: 700;
    font-size: 39px; line-height: 46px; letter-spacing: 0.8px;
    color: var(--alert-red);
  }
  .promise {
    position: absolute; left: 0; width: 1208px; top: 250px;
    text-align: center; margin: 0;
    font-family: "Open Sans", sans-serif;
    font-size: 28px; line-height: 35px; letter-spacing: 2px;
  }
  .values {
    position: absolute; left: 0; width: 1217px; top: 327px;
    text-align: center; margin: 0;
    font-family: "Open Sans", sans-serif; font-weight: 700;
    font-size: 27px; line-height: 34px; letter-spacing: 2.8px;
  }
  .team-photo {
    position: absolute; left: 160px; top: 373px; width: 340px; height: 315px;
    background: linear-gradient(135deg, var(--photo-light), var(--photo-dark));
  }
  .team-names {
    position: absolute; left: 158px; top: 692px; width: 342px;
    display: flex; justify-content: space-between;
    font-family: "Open Sans", sans-serif; font-weight: 700;
    font-size: 21px; line-height: 30px;
  }
  .services {
    position: absolute; left: 585px; top: 378px; margin: 0;
    font-family: "Open Sans", sans-serif;
    font-size: 32px; line-height: 40.3px; letter-spacing: 2.3px;
  }
  .services-heading { font-weight: 700; font-style: italic; margin-left: 13px; font-size: 31px; letter-spacing: 3.5px; }
  .services ul { list-style: none; margin: 0; padding: 0; }
  .services li::before { content: ">"; }
  .phone {
    position: absolute; left: 236px; top: 712px; margin: 0;
    font-family: "Arimo", sans-serif; font-weight: 700;
    color: var(--alert-red);
    white-space: nowrap;
  }
  .phone .area { font-size: 78px; letter-spacing: 10px; }
  .phone .number { font-size: 116px; letter-spacing: 7px; }
  .contact {
    position: absolute; left: 0; width: 1176px; top: 832px;
    text-align: center; margin: 0;
    font-family: "Open Sans", sans-serif; font-weight: 700;
    font-size: 26px; line-height: 28px; letter-spacing: 2.6px;
  }
</style>
</head>
<body>
<div class="ad">
  <header class="masthead">
    <h1 class="firm-name">Thornbury &amp; Lisle<sup>PLLC</sup></h1>
  </header>

  <h2 class="practice">WORKERS’ COMPENSATION</h2>
  <p class="credential">Former Assistant Attorneys General Who Know The System</p>
  <p class="promise">At Thornbury &amp; Lisle, We Provide Personal Attention To Our Clients..<br>That Means Your Case is Handled By An Attorney, Not An Assistant.</p>
  <p class="values">PROFESSIONAL-COMMITTED-EFFECTIVE</p>

  <div class="team-photo" role="img" aria-label="Photo of the two attorneys standing in a law library, one holding an open book"></div>
  <div class="team-names"><span>Owen Thornbury</span><span>Claire Lisle</span></div>

  <section class="services">
    <div class="services-heading">We Can Help With:</div>
    <ul>
      <li>Workplace Injuries Or Death</li>
      <li>Lost Wages</li>
      <li>Medical Expenses &amp; Treatment</li>
      <li>Hearing Loss Claims</li>
      <li>Pensiom Claims</li>
      <li>Disability Awards</li>
      <li>Return To Work Issues</li>
    </ul>
  </section>

  <p class="phone"><span class="area">360</span><span class="number">555-0142</span></p>
  <p class="contact">227 N. Cornwall Suite 540, Bellingham<br>www.thornburylisle.com</p>
</div>
</body>
</html>
```